Business card based on your logo design "Marlowe&Co"

Can you please design a business card based on the logo artwork you designed for our business. Double sided as per your submitted image of possible application of logo.

```html
<!DOCTYPE html>
<html lang="en">
<head>
<meta charset="utf-8">
<title>Marlowe&amp;Co — Business Card</title>
<link href="https://fonts.googleapis.com/css2?family=Exo+2:wght@300;400;700&display=swap" rel="stylesheet">
<style>
  :root {
    --backdrop: #e4e2df;
    --card: #38393b;
    --card-edge: #2e2f31;
    --ink: #f2f2f2;
    --ink-soft: #c9c9c9;
    --accent: #f7931e;
  }
  * { margin: 0; padding: 0; box-sizing: border-box; }
  html, body {
    width: 1200px; height: 576px; overflow: hidden;
    background: var(--backdrop);
    font-family: "Exo 2", sans-serif;
  }
  .sheet {
    width: 1200px; height: 576px;
    display: flex; align-items: center; justify-content: center; gap: 60px;
  }
  .card {
    position: relative;
    width: 520px; height: 297px;
    background: var(--card);
    border: 1px solid var(--card-edge);
    border-radius: 6px;
    box-shadow: 0 6px 18px rgba(0,0,0,.18);
    color: var(--ink);
  }
  .brand {
    display: flex; align-items: center; gap: 10px;
  }
  .brand-mark {
    width: 14px; height: 14px; background: var(--accent);
  }
  .brand-name {
    font-weight: 700; letter-spacing: 1px; color: var(--ink);
  }
  .brand-tagline {
    font-weight: 400; color: var(--ink-soft); letter-spacing: .5px;
  }

  /* back side */
  .card-back .brand { position: absolute; left: 30px; top: 34px; }
  .card-back .brand-name { font-size: 28px; }
  .card-back .brand-tagline { position: absolute; left: 30px; top: 76px; font-size: 9px; }
  .person { position: absolute; left: 250px; top: 110px; }
  .person-name { font-size: 24px; font-weight: 400; letter-spacing: 1px; }
  .person-role { font-size: 12px; color: var(--accent); margin-left: 42px; margin-top: -2px; }
  .contact {
    position: absolute; right: 30px; top: 158px;
    font-size: 13px; font-weight: 300; line-height: 22px; text-align: right;
  }
  .address {
    position: absolute; left: 30px; bottom: 34px;
    font-size: 13px; font-weight: 300; line-height: 22px;
    display: flex; gap: 8px;
  }
  .address svg { margin-top: 4px; flex: none; }

  /* front side */
  .card-front { display: flex; flex-direction: column; align-items: center; justify-content: center; gap: 10px; }
  .card-front .brand-name { font-size: 46px; }
  .card-front .brand-mark { width: 20px; height: 20px; }
  .card-front .brand-tagline { font-size: 12px; }
</style>
</head>
<body>
<main class="sheet">
  <section class="card card-back" aria-label="Card back">
    <div class="brand">
      <span class="brand-name">MARLOWE&amp;CO</span>
      <span class="brand-mark"></span>
    </div>
    <p class="brand-tagline">Building and Project Management</p>

    <div class="person">
      <p class="person-name">Jordan Reyes</p>
      <p class="person-role">director</p>
    </div>

    <div class="contact">
      <p>0123 456 7890</p>
      <p>info@marloweandco.com</p>
      <p>www.marloweandco.com</p>
    </div>

    <div class="address">
      <svg width="14" height="12" viewBox="0 0 14 12" aria-hidden="true">
        <path d="M7 0 L14 6 H12 V12 H8.5 V8 H5.5 V12 H2 V6 H0 Z" fill="var(--accent)"/>
      </svg>
      <p>Harbor Lane 48<br>Riverton 31562<br>U.S.A</p>
    </div>
  </section>

  <section class="card card-front" aria-label="Card front">
    <div class="brand">
      <span class="brand-name">MARLOWE&amp;CO</span>
      <span class="brand-mark"></span>
    </div>
    <p class="brand-tagline">Building and Project Management</p>
  </section>
</main>
</body>
</html>
```